Newsletter-Design für Garten-Samen Shop
Zielgruppe
Online Shop für Obst-, Gemüse-, Kräuter- und Pflanzensamen
Aufgabenstellung
www.beetfreunde-portal.example ist die Seite mit den Produkten. Als Tipp sollte das Jiaogulan genannt werden da dieses Produkt sich am meisten verkauft.

```html
<!DOCTYPE html>
<html lang="de">
<head>
<meta charset="utf-8">
<title>Beetfreunde Newsletter 01/17</title>
<link href="https://fonts.googleapis.com/css2?family=Open+Sans:wght@400;600;700;800&display=swap" rel="stylesheet">
<style>
:root{
  --green:#86a80a;
  --hero-green:#9bbb1a;
  --stage:#bdbec3;
  --ink:#3b4550;
  --text:#2e2e2e;
  --muted:#6a6f75;
  --soft:#f7f7f7;
  --white:#fff;
}
*{box-sizing:border-box;margin:0;padding:0}
html,body{width:1200px;height:4164px;overflow:hidden}
body{background:var(--stage);font-family:"Open Sans",Arial,sans-serif;color:var(--text);position:relative}
.abs{position:absolute}
.webversion{top:150px;left:0;width:1200px;text-align:center;font-size:14px;color:var(--white)}
.mail{left:186px;top:186px;width:828px;height:3836px;background:var(--white);box-shadow:0 10px 30px rgba(0,0,0,.25);overflow:hidden}
.mail>*{position:absolute}
.brand-name{font-weight:700;font-size:36px;letter-spacing:-1.5px;color:var(--white);line-height:1}
.brand-tag{font-weight:600;font-size:15px;color:var(--white)}
.hero{left:0;top:0;width:828px;height:560px}
.hero-title{left:60px;top:230px;font-weight:700;font-size:74px;line-height:74px;color:var(--white);letter-spacing:-1px}
.issue{right:60px;top:60px;font-size:14px;font-weight:600;color:var(--white)}
.badge{left:597px;top:438px;width:168px;height:168px;border-radius:50%;background:var(--white);box-shadow:0 4px 10px rgba(0,0,0,.25);display:flex;align-items:center;justify-content:center}
.badge-ring{width:150px;height:150px;border-radius:50%;border:4px solid var(--green);display:flex;align-items:center;justify-content:center;text-align:center;color:var(--green);font-weight:700;font-size:23px;line-height:23px;transform:rotate(12deg)}
.sec-title{font-weight:600;font-size:27px;color:var(--ink)}
.sec-sub{font-size:15px;color:var(--muted)}
.prod-title{left:60px;top:768px;font-size:31px;color:var(--green);font-weight:600}
.prod-sub{left:60px;top:806px;font-size:20px;color:var(--text)}
.copy{left:60px;width:708px;font-size:17.5px;line-height:29.5px;color:var(--text);hyphens:manual}
.copy a{color:var(--green);text-decoration:none}
.benefits{left:60px;top:1166px;width:706px;font-size:23px;line-height:30px;font-weight:700;color:var(--green)}
.soft-band{left:0;top:1880px;width:828px;height:840px;background:var(--soft)}
.plants{left:0;top:1334px;width:828px;height:612px}
.soft-end{left:0;top:2660px;width:828px;height:80px}
.pct{left:64px;top:1780px;width:98px;height:98px;background:var(--green);border-radius:8px;transform:rotate(-8deg);box-shadow:0 4px 10px rgba(0,0,0,.3);color:var(--white);font-size:58px;display:flex;align-items:center;justify-content:center}
.price{left:205px;top:1826px;color:var(--white);font-weight:700;font-size:46px;line-height:60px}
.price s{font-size:22px;font-weight:600;margin-right:6px}
.btn{display:flex;align-items:center;justify-content:center;font-weight:600;font-size:18px;border-radius:3px}
.btn-white{left:495px;top:1834px;width:272px;height:48px;background:var(--white);color:var(--green)}
.rec{width:210px;text-align:center}
.rec-photo{width:210px;height:210px;border-radius:50%;position:relative}
.rec-photo::after{content:"";position:absolute;inset:12px;border-radius:50%;border:3px solid rgba(255,255,255,.9)}
.rec-name{margin-top:38px;font-size:20px;line-height:22px;color:var(--ink)}
.rec-qty{margin-top:28px;font-size:17px;color:var(--ink)}
.btn-green{margin-top:30px;height:49px;background:var(--green);color:var(--white)}
.post{width:370px;display:flex;gap:12px}
.post-thumb{width:87px;height:87px;flex:none}
.post h4{font-weight:600;font-size:18px;color:var(--green)}
.post p{font-size:13.5px;line-height:20px;color:var(--ink);margin-top:4px}
.btn-outline{left:60px;top:3213px;width:212px;height:49px;border:3px solid var(--green);color:var(--green);background:var(--white)}
.footer{left:0;top:3380px;width:828px;height:456px}
.follow{right:60px;top:3532px;display:flex;align-items:center;gap:18px;color:var(--white);font-weight:600;font-size:16px}
.follow span.dot{width:38px;height:38px;border-radius:50%;background:var(--white)}
.legal{left:60px;width:720px;font-size:13px;line-height:22px;color:rgba(255,255,255,.78)}
</style>
</head>
<body>
<div class="abs webversion">Probleme mit der Darstellung? Die Webversion finden Sie hier .</div>

<main class="abs mail">
  <svg class="hero" viewBox="0 0 828 560" role="img" aria-label="Foto frischer Gemüse in grüner Tönung">
    <defs><linearGradient id="hg" x1="0" y1="0" x2="1" y2="1"><stop offset="0" stop-color="#a7c523"/><stop offset="1" stop-color="#93b412"/></linearGradient></defs>
    <path d="M0 0H828V444C650 500 420 556 0 558Z" fill="url(#hg)"/>
  </svg>
  <div class="brand-name" style="left:62px;top:52px">Beetfreunde</div>
  <div class="brand-tag" style="left:62px;top:96px">Obst, Gemüse + Pflanzen</div>
  <div class="issue">NEWSLETTER 01 / 17</div>
  <h1 class="hero-title">Jetzt in das<br>Frühjahr starten!</h1>
  <div class="badge"><div class="badge-ring">NEU IM<br>ANGEBOT</div></div>

  <h2 class="sec-title" style="left:60px;top:628px">Unsere Top-Empfehlung</h2>
  <div class="sec-sub" style="left:60px;top:670px">Das Angebot des Monats</div>

  <h3 class="prod-title">Jiaogulan – Kraut der Unsterblichkeit – 50 Samen</h3>
  <div class="prod-sub">Jetzt Pflanzsamen endlich auch in Deutschland!</div>
  <p class="copy" style="top:877px">50 Samen vom Kraut der Unsterblichkeit zum selbst aussähen. Jiaogulan ist eine aus&shy;dauernde, krautige, bodendeckende Pflanze. Einfach und leicht anzubauen (<a href="#">siehe Blog-Artikel</a>).</p>
  <p class="copy" style="top:997px">Jiaogulan ist eine traditionelle asiatische Heilpflanze, die aufgrund zahlreicher interna&shy;tionaler Studien in unseren Breitengraden immer stärker an Beachtung gewinnt. So wurde die Wirkkraft bei der Bekämpfung von modernen, westlichen Zivilisationskrank&shy;heiten zweifelsfrei festgestellt, u.a.:</p>
  <p class="benefits">Erschöpfung, Kopfschmerzen, Kreislaufbeschweren, Erkältungen, Entzündungen, Hyperviskosität, Stress und Einschlafprobleme</p>

  <div class="soft-band"></div>
  <svg class="plants" viewBox="0 0 828 612">
    <defs><linearGradient id="lg" x1="0" y1="0" x2="0" y2="1"><stop offset="0" stop-color="#5d9a33"/><stop offset="1" stop-color="#2f6a1e"/></linearGradient></defs>
    <path role="img" aria-label="Foto dichter Jiaogulan-Blätter" d="M0 60C120 20 250 40 400 8C560 30 700 20 828 55V460H0Z" fill="url(#lg)"/>
    <path d="M0 445C300 425 560 420 828 412V611C560 600 300 582 0 566Z" fill="var(--green)"/>
  </svg>
  <div class="pct">%</div>
  <div class="price"><s>8,99€</s>7,99€</div>
  <a class="abs btn btn-white">Jetzt bestellen</a>

  <h2 class="sec-title" style="left:60px;top:2022px">Weitere Empfehlungen</h2>
  <div class="sec-sub" style="left:60px;top:2064px">Bringen Sie Gesundheit in Ihren Garten</div>

  <div class="rec" style="left:61px;top:2164px">
    <div class="rec-photo" role="img" aria-label="Foto Liebstöckel" style="background:radial-gradient(#7dab4a,#3f7526)"></div>
    <div class="rec-name">Liebstöckel /<br>Maggikraut</div>
    <div class="rec-qty">ca. 50 Samen</div>
    <div class="btn btn-green">Jetzt bestellen</div>
  </div>
  <div class="rec" style="left:309px;top:2164px">
    <div class="rec-photo" role="img" aria-label="Foto Bärlauch mit Blüten" style="background:radial-gradient(#6f9e46,#2e5e1e)"></div>
    <div class="rec-name">Bärlauch /<br>Waldknoblauch</div>
    <div class="rec-qty">ca. 50 Samen</div>
    <div class="btn btn-green">Jetzt bestellen</div>
  </div>
  <div class="rec" style="left:557px;top:2164px">
    <div class="rec-photo" role="img" aria-label="Foto Stevia-Pflanze" style="background:radial-gradient(#8cc24e,#3c7a22)"></div>
    <div class="rec-name">Stevia /<br>Zuckerersatz</div>
    <div class="rec-qty">ca. 100 Samen</div>
    <div class="btn btn-green">Jetzt bestellen</div>
  </div>

  <svg class="soft-end" viewBox="0 0 828 80">
    <path d="M0 30C250 62 580 62 828 26V80H0Z" fill="var(--white)"/>
  </svg>

  <h2 class="sec-title" style="left:60px;top:2806px">Neues aus unserem Blog</h2>
  <div class="sec-sub" style="left:60px;top:2848px">Tipps und Trends zum Thema Bepflanzung</div>
  <p class="copy" style="top:2905px">In unserem <a href="#">Blog</a> finden Sie viele interessante Beiträge und Nachrichten rund um das Thema Garten. Falls Sie etwas verpasst haben, hier die zwei neuesten Beiträge direkt aus unserem Blog.</p>

  <div class="post" style="left:63px;top:3059px">
    <div class="post-thumb" role="img" aria-label="Foto Flammenbaum-Blüten" style="background:linear-gradient(135deg,#d8282a,#6a8a2a)"></div>
    <div><h4>Flammenbaum</h4><p>Der Flammenbaum erreicht in unseren Breiten eine Höhe von drei bis zehn Metern...</p></div>
  </div>
  <div class="post" style="left:414px;top:3059px">
    <div class="post-thumb" role="img" aria-label="Foto Kornblume" style="background:linear-gradient(135deg,#2c4fb8,#b8c630)"></div>
    <div><h4>Kornblume</h4><p>Die Kornblume mit ihren blauen bis violetten Blütenkörben dürfte den meisten im deutschen...</p></div>
  </div>
  <a class="abs btn btn-outline">Mehr Artikel</a>

  <svg class="footer" viewBox="0 0 828 456">
    <path d="M0 11C280 90 560 92 828 80V456H0Z" fill="var(--green)"/>
  </svg>
  <div class="brand-name" style="left:62px;top:3495px">Beetfreunde</div>
  <div class="brand-tag" style="left:62px;top:3539px">Obst, Gemüse + Pflanzen</div>
  <div class="abs follow">Folgen Sie uns <span class="dot"></span></div>
  <div class="legal" style="top:3626px">Lomzu Saatgut GmbH . Lindenweg 12 . 34567 Grünfelden . Deutschland<br>Tel. +49 00000 123456 &nbsp;|&nbsp; info@lomzu.example &nbsp;|&nbsp; USt-IdNr.: DE000000000<br>Eingetragen im Handelsregister des Amtsgerichtes Grünfelden &nbsp;|&nbsp; Handelsregisternummer HRB 0000</div>
  <div class="legal" style="top:3710px">Damit diese E-Mail zuverlässig in Ihren Posteingang zugestellt wird, fügen Sie bitte info@lomzu.example zu Ihrem Adressbuch hinzu. Sie möchten keine weiteren Informationen erhalten? Dann bitte hier austragen!</div>
  <div class="legal" style="top:3770px">© 2017 Beetfreunde | AGB | Impressum | Datenschutz</div>
</main>
</body>
</html>
```